Dewleaf Botanica. Home based organic skin care manufacturer

We need top notch user friendly and interactive web6/mobile site that will cater to online e commerce, retail of our varieties of products and real time communication with online buyers.

```html
<!DOCTYPE html>
<html lang="en">
<head>
<meta charset="utf-8">
<title>Dewleaf Botanica – Home Based Organic Skin Care</title>
<link href="https://fonts.googleapis.com/css2?family=Montserrat:wght@400;500;600;700&display=swap" rel="stylesheet">
<style>
:root{
  --rose:#d3a19b;
  --rose-deep:#b87f78;
  --rose-soft:#e5c2bd;
  --blush:#f6efee;
  --blush-2:#f3e8e6;
  --ink:#3d2b28;
  --text:#5a4a47;
  --muted:#8d7e7b;
  --night:#382824;
  --white:#ffffff;
}
*{box-sizing:border-box;margin:0;padding:0}
html,body{width:1200px;height:4054px;overflow:hidden}
body{position:relative;background:var(--white);font-family:"Montserrat",sans-serif;color:var(--text)}
.abs{position:absolute}
.btn{position:absolute;background:var(--rose);color:var(--white);font-size:11px;letter-spacing:1.5px;display:flex;align-items:center;justify-content:center;text-transform:uppercase;white-space:nowrap}
.photo{position:absolute}
.section-title{position:absolute;left:0;width:1200px;text-align:center;font-weight:600;color:var(--ink);font-size:22px;letter-spacing:1px}

/* announcement */
.announce{top:0;left:0;width:1200px;height:33px;background:var(--rose);color:var(--white);font-size:10.5px;display:flex;align-items:center;justify-content:center;letter-spacing:.3px}

/* hero */
.hero{top:33px;left:0;width:1200px;height:587px;background:linear-gradient(180deg,#f7f0ef 0%,#f3e6e3 100%)}
.brand{font-family:"Montserrat",sans-serif;font-weight:500;color:var(--ink);font-size:15px;letter-spacing:1.5px;text-transform:uppercase;display:flex;align-items:center;gap:8px;white-space:nowrap}
.brand .dot{width:12px;height:12px;border-radius:50%;background:var(--rose)}
.site-brand{top:60px;left:31px}
.nav{top:64px;left:478px;width:594px;display:flex;justify-content:space-between;font-size:11.5px;letter-spacing:1.2px;color:var(--ink);white-space:nowrap}
.nav-icons{top:62px;left:1091px;display:flex;gap:16px}
.hero-badge{top:244px;left:300px;width:209px;height:32px;background:var(--rose-deep);color:var(--white);font-size:13px;letter-spacing:.5px;display:flex;align-items:center;justify-content:center}
.hero-title{top:298px;left:150px;width:510px;text-align:center;font-weight:600;font-size:38px;line-height:42px;color:var(--ink);letter-spacing:.5px}
.hero-copy{top:393px;left:205px;width:400px;text-align:center;font-size:15.5px;line-height:26px;color:var(--ink)}
.hero-btn{top:469px;left:342px;width:126px;height:37px}
.hero-photo{top:107px;left:630px;width:500px;height:480px;background:radial-gradient(ellipse at 50% 40%,#ecc7b5 0%,#e3b7a6 40%,#f0dcd5 75%,rgba(243,230,227,0) 100%)}

/* newsletter */
.news-input{top:672px;left:337px;width:403px;height:38px;border:1px solid #d9cbc9;background:var(--white);font-size:11px;color:#b4a8a6;padding-left:20px;display:flex;align-items:center}
.news-btn{top:672px;left:745px;width:118px;height:38px;font-size:11px;letter-spacing:.3px;text-transform:none}

/* offers */
.offers-bg{top:710px;left:0;width:1200px;height:427px;background:linear-gradient(180deg,#fbf7f6 0%,#ffffff 100%)}
.offer{position:absolute;width:260px;text-align:center}
.offer .ring{width:211px;height:211px;border-radius:50%;border:7px solid #cb9c96;margin:0 auto;overflow:hidden}
.offer .ring div{width:100%;height:100%;border-radius:50%;border:4px solid #fff}
.offer h3{font-size:14px;font-weight:600;color:var(--ink);letter-spacing:.8px;margin-top:27px}
.offer p{font-size:12px;color:var(--rose);margin-top:7px}

/* about */
.about-bg{top:1137px;left:0;width:602px;height:343px;background:var(--blush)}
.about-photo{top:1137px;left:602px;width:598px;height:343px;background:linear-gradient(120deg,#e9dcd8 0%,#d8c2b6 45%,#efe2dc 100%)}
.about-title{top:1182px;left:200px;font-size:27px;font-weight:600;color:var(--ink);letter-spacing:1px}
.about-copy{top:1231px;left:200px;width:380px;font-size:11.2px;line-height:19.5px;color:var(--text)}
.about-copy p+p{margin-top:6px}
.about-btn{top:1397px;left:200px;width:107px;height:33px}

/* experts */
.feature-panel{position:absolute;background:var(--blush)}
.feature-title{position:absolute;font-size:24.5px;font-weight:600;line-height:33px;color:var(--ink);white-space:nowrap}
.feature-copy{position:absolute;font-size:11.2px;line-height:19.3px;color:var(--text)}

/* products */
.products-bg{top:2422px;left:0;width:1200px;height:678px;background:var(--blush)}
.product{position:absolute;top:2518px;width:186px;text-align:center}
.product .pack{height:193px;position:relative}
.product .sale{position:absolute;top:6px;right:6px;background:var(--rose-soft);color:#fff;font-size:8px;padding:2px 5px;letter-spacing:.5px}
.product h4{font-weight:400;font-size:14.5px;color:var(--ink);margin-top:18px;white-space:nowrap}
.product p{font-size:13px;color:var(--rose);margin-top:4px}
.all-btn{top:2796px;left:529px;width:142px;height:33px;border:1.5px solid #9a8d8b;color:var(--ink);font-size:11px;letter-spacing:2px;display:flex;align-items:center;justify-content:center;background:transparent}

/* video */
.video{top:2942px;left:272px;width:656px;height:318px;background:linear-gradient(110deg,#5c4a44 0%,#a88676 35%,#c9a18e 55%,#7a6259 100%)}
.play{top:3071px;left:570px;width:60px;height:60px;border-radius:50%;background:rgba(255,255,255,.95)}

/* testimonials */
.testimonial{position:absolute;top:3366px;width:391px;height:204px;background:#fbf7f6;border-radius:6px;box-shadow:0 1px 6px rgba(120,90,85,.12);text-align:center}
.testimonial .stars{margin-top:22px;display:flex;gap:3px;justify-content:center}
.testimonial blockquote{font-size:11px;line-height:19px;color:var(--text);width:340px;margin:22px auto 0}
.testimonial hr{width:46px;border:0;border-top:1px solid var(--rose);margin:16px auto 0}
.testimonial cite{display:block;font-style:normal;font-weight:600;font-size:11.5px;color:var(--ink);margin-top:10px}
.testimonial small{display:block;font-size:10px;color:var(--text);margin-top:3px}
.dots{top:3605px;left:578px;display:flex;gap:7px}
.dots span{width:9px;height:9px;border-radius:50%;border:1px solid #b7aaa8}
.dots span.on{background:var(--rose);border-color:var(--rose)}

/* footer */
.footer{top:3671px;left:0;width:1200px;height:383px;background:var(--night);color:#e9dfdd}
.signup{top:3720px;left:200px;font-weight:600;font-size:16px;letter-spacing:.8px;color:#fff}
.footer-input{top:3714px;left:610px;width:302px;height:33px;background:#fff;font-size:10.5px;color:#b5aaa8;padding-left:18px;display:flex;align-items:center}
.footer-btn{top:3714px;left:912px;width:88px;height:33px;font-size:11px;text-transform:none;letter-spacing:.3px}
.footer-brand{top:3849px;left:200px;color:#fff;font-size:12px;letter-spacing:1.2px}
.footer-col{position:absolute;top:3811px}
.footer-col h5{font-size:13px;font-weight:600;letter-spacing:.6px;color:#fff;margin-bottom:10px}
.footer-col li{list-style:none;font-size:11px;line-height:22.7px;color:#e9dfdd;white-space:nowrap}
.footer-col li.link:before{content:"›";margin-right:9px;color:#b7aaa8}
.socials{display:flex;gap:11px;margin-top:8px}
.socials span{width:12px;height:12px;border-radius:50%;background:var(--rose)}
.copyright{top:4012px;left:0;width:1200px;text-align:center;font-size:10.5px;color:#e9dfdd}
</style>
</head>
<body>

<div class="abs announce">Choose a beauty gift. FREE when you spend $99.00. See Details</div>

<section class="abs hero">
  <div class="photo hero-photo" role="img" aria-label="Smiling woman touching her glowing skin"></div>
</section>

<div class="abs brand site-brand"><span class="dot"></span>Dewleaf Botanica</div>

<nav class="abs nav">
  <span>HOME</span><span>ABOUT</span><span>SKIN CARE</span><span>BODY CARE</span><span>OUR TREATMENTS</span><span>CONTACT</span>
</nav>
<div class="abs nav-icons">
  <svg width="16" height="16" viewBox="0 0 16 16" fill="none" stroke="#3d2b28" stroke-width="1.6"><circle cx="6.5" cy="6.5" r="5"/><line x1="10.3" y1="10.3" x2="15" y2="15"/></svg>
  <svg width="16" height="16" viewBox="0 0 16 16" fill="none" stroke="#3d2b28" stroke-width="1.4"><circle cx="8" cy="5" r="3.5"/><path d="M1.5 15.5c0-3.6 2.9-5.5 6.5-5.5s6.5 1.9 6.5 5.5"/></svg>
  <svg width="17" height="16" viewBox="0 0 17 16" fill="none" stroke="#d3a19b" stroke-width="1.4"><path d="M1 1.5h2.5l2 9h8.5l1.8-6.5H4.5"/><circle cx="6.5" cy="14" r="1.2"/><circle cx="13" cy="14" r="1.2"/></svg>
</div>

<div class="abs hero-badge">40% OFF ON PRODUCTS</div>
<h1 class="abs hero-title">HOME BASED<br>ORGANIC SKIN CARE</h1>
<p class="abs hero-copy">Bringing you a range of high-quality skin care made from 100% organic</p>
<div class="btn hero-btn">Learn More&nbsp;→</div>

<div class="abs offers-bg"></div>
<div class="abs news-input">Email Address</div>
<div class="btn news-btn">Get Noticed</div>

<h2 class="section-title" style="top:770px">WHAT WE OFFERS</h2>
<div class="offer" style="top:820px;left:197px">
  <div class="ring"><div role="img" aria-label="Woman holding a jar of organic cream among leaves" style="background:linear-gradient(135deg,#6f8a5a,#d9b9a6 60%,#f0e6df)"></div></div>
  <h3>ORGANIC SOLUTION</h3><p>Get the promo</p>
</div>
<div class="offer" style="top:820px;left:470px">
  <div class="ring"><div role="img" aria-label="Client receiving a facial treatment" style="background:linear-gradient(135deg,#dfe3e8,#e9c9bd 55%,#f4ece9)"></div></div>
  <h3>TREATMENT</h3><p>Start from $25.00</p>
</div>
<div class="offer" style="top:820px;left:742px">
  <div class="ring"><div role="img" aria-label="Cream jars with cucumber slices and oil bottles" style="background:linear-gradient(135deg,#f4f1ea,#e8ecd6 50%,#d8c27a)"></div></div>
  <h3>EXCELLENT OFFERS</h3><p>Get the promo</p>
</div>

<div class="abs about-bg"></div>
<div class="photo about-photo" role="img" aria-label="Woman applying cream in front of a lit vanity mirror"></div>
<h2 class="abs about-title">ABOUT US</h2>
<div class="abs about-copy">
  <p>Welcome to Dewleaf Botanica, Home based organic skin care manufacturer, bringing you a range of high-quality skin care made from 100% organic. Lorem ipsum dolor sit amet, consectetur adipiscing elit, sed do eiusmod tempor incididunt ut labore magn.</p>
  <p>Diam volutpat commodo sed egestas. Nisi quis eleifend quam adipiscing vitae proin sagittis nisl. Nulla malesuada pellentes elit eget gravida cum sociis natoque penatibus.</p>
</div>
<div class="btn about-btn">View More</div>

<h2 class="section-title" style="top:1527px;line-height:28px">CONNECTING YOU WITH EXPERTS IN<br>SKIN CARE AND TREATMENTS</h2>

<div class="feature-panel" style="top:1649px;left:315px;width:685px;height:356px"></div>
<div class="photo" role="img" aria-label="Therapist brushing a clay mask onto a client's face" style="top:1613px;left:200px;width:369px;height:327px;background:linear-gradient(135deg,#c9b2a5,#8fa79a 50%,#e6d8cf)"></div>
<svg class="abs" style="top:1688px;left:614px" width="44" height="56" viewBox="0 0 44 56" fill="none" stroke="#c9928b" stroke-width="1.3"><ellipse cx="22" cy="18" rx="10" ry="12"/><path d="M12 14c2-8 18-8 20 0M10 52c0-10 5-16 12-16s12 6 12 16M4 52c2-8 4-12 8-16M40 52c-2-8-4-12-8-16"/></svg>
<h3 class="feature-title" style="top:1759px;left:610px">Only pay if your condition<br>improves after treatment</h3>
<p class="feature-copy" style="top:1836px;left:610px;width:375px">Lorem ipsum dolor sit amet, consectetur adipiscing elit, sed do eiusmod tempor incididunt ut labore magn. Diam volutpat com sed egestas. Nisi quis eleifend quam adipiscing vitae proin sagittis nisl. Nulla malesuada pellentes elit eget.</p>
<div class="btn" style="top:1934px;left:610px;width:107px;height:32px">View More</div>

<div class="feature-panel" style="top:2155px;left:610px;width:590px;height:259px"></div>
<div class="photo" role="img" aria-label="Woman holding white flowers to her face" style="top:2057px;left:635px;width:365px;height:332px;background:linear-gradient(135deg,#9aa38e,#e7cdbd 50%,#f2e7e1)"></div>
<svg class="abs" style="top:2113px;left:200px" width="54" height="40" viewBox="0 0 54 40" fill="none" stroke="#c9928b" stroke-width="1.4"><rect x="2" y="12" width="34" height="24" rx="3"/><ellipse cx="40" cy="18" rx="12" ry="14"/><path d="M2 20h34"/></svg>
<h3 class="feature-title" style="top:2173px;left:200px">Speak to a professional<br>without the in person</h3>
<p class="feature-copy" style="top:2250px;left:200px;width:375px">Lorem ipsum dolor sit amet, consectetur adipiscing elit, sed do eiusmod tempor incididunt ut labore magn. Diam volutpat com sed egestas. Nisi quis eleifend quam adipiscing vitae proin sagittis nisl. Nulla malesuada pellentes elit eget.</p>
<div class="btn" style="top:2348px;left:200px;width:107px;height:32px">View More</div>

<div class="abs products-bg"></div>
<h2 class="section-title" style="top:2464px">TOP SELLING PRODUCTS</h2>
<div class="product" style="left:200px">
  <div class="pack" role="img" aria-label="Age reverse serum package" style="background:#f1e8d4"><span class="sale">SALE</span></div>
  <h4>Age Reverse Serum</h4><p>£12.99</p>
</div>
<div class="product" style="left:405px">
  <div class="pack" role="img" aria-label="Balancing facial toner package" style="background:#f7f5f4;border:1px solid #e8e1df"><span class="sale">SALE</span></div>
  <h4>Balancing Facial Toner</h4><p>£12.99</p>
</div>
<div class="product" style="left:610px">
  <div class="pack" role="img" aria-label="Brightening body milk package" style="background:#f8f7f9;border:1px solid #e8e1df"></div>
  <h4>Brightening Body Milk</h4><p>£12.99</p>
</div>
<div class="product" style="left:814px">
  <div class="pack" role="img" aria-label="Brightening body wash package" style="background:#b39ccc"></div>
  <h4>Brightening Body Wash</h4><p>£12.99</p>
</div>
<div class="abs all-btn">ALL PRODUCTS</div>

<h2 class="section-title" style="top:2894px">HOW IT WORKS</h2>
<div class="photo video" role="img" aria-label="Video preview of a woman applying face cream"></div>
<div class="abs play"></div>
<svg class="abs" style="top:3089px;left:592px" width="20" height="24" viewBox="0 0 20 24"><path d="M2 2l16 10L2 22z" fill="#5a4a47"/></svg>

<h2 class="section-title" style="top:3308px">TESTIMONIALS</h2>
<div class="testimonial" style="left:200px">
  <div class="stars">
    <svg width="80" height="13" viewBox="0 0 80 13" fill="#d3a19b"><g id="s"><path d="M6.5 0l1.9 4.2 4.6.5-3.4 3.1 1 4.5-4.1-2.4-4.1 2.4 1-4.5L0 4.7l4.6-.5z"/></g><use href="#s" x="16.5"/><use href="#s" x="33"/><use href="#s" x="49.5"/><use href="#s" x="66"/></svg>
  </div>
  <blockquote>Diam volutpat commodo sed egestas. Nisi quis eleifend quam adipiscing vitae proin sagittis nisl. Nulla malesuada pellentes elit eget gravida cum sociis natoque et ut labore.</blockquote>
  <hr><cite>MARA ELLISON</cite><small>Director, Lorem Company</small>
</div>
<div class="testimonial" style="left:610px">
  <div class="stars">
    <svg width="80" height="13" viewBox="0 0 80 13" fill="#d3a19b"><use href="#s"/><use href="#s" x="16.5"/><use href="#s" x="33"/><use href="#s" x="49.5"/><use href="#s" x="66"/></svg>
  </div>
  <blockquote>Diam volutpat commodo sed egestas. Nisi quis eleifend quam adipiscing vitae proin sagittis nisl. Nulla malesuada pellentes elit eget gravida cum sociis natoque et ut labore.</blockquote>
  <hr><cite>MARA ELLISON</cite><small>Director, Lorem Company</small>
</div>
<div class="abs dots"><span></span><span class="on"></span><span></span></div>

<footer class="abs footer"></footer>
<div class="abs signup">SIGN UP AND SAVE</div>
<div class="abs footer-input">Enter your email address</div>
<div class="btn footer-btn">Subscribe</div>
<div class="abs brand footer-brand"><span class="dot"></span>Dewleaf Botanica</div>
<div class="footer-col" style="left:406px">
  <h5>TREATMENTS</h5>
  <ul><li class="link">Skin Care</li><li class="link">Body Care</li><li class="link">Nails</li><li class="link">Appliances</li></ul>
</div>
<div class="footer-col" style="left:610px">
  <h5>QUICK LINKS</h5>
  <ul><li class="link">About us</li><li class="link">Contact us</li><li class="link">Blog</li><li class="link">FAQ</li><li class="link">Privacy Policy</li><li class="link">Terms and Conditions</li></ul>
</div>
<div class="footer-col" style="left:835px">
  <h5>ADDRESS</h5>
  <ul><li>14 Linden Row</li><li>Harbourside HB2 4RT</li><li>Mob: 020 5550 1842</li><li>E-mail: info@dewleafbotanica.com</li></ul>
  <div class="socials"><span></span><span></span><span></span></div>
</div>
<div class="abs copyright">© Dewleaf Botanica 2023. All rights reserved.</div>

</body>
</html>
```